Business Card Design - Law Firm

I need a business card design. I have attached a picture of the law firm's website and logo. The business card design should be consistent with those pictures. There should be a place for the employee name, employee job title, telephone number, facsimile number, address, website url, and email address for each employee.
Industry/Entity Type
Business

```html
<!DOCTYPE html>
<html lang="en">
<head>
<meta charset="utf-8">
<title>Aldermere Law – Business Card</title>
<link rel="stylesheet" href="https://fonts.googleapis.com/css2?family=Libre+Bodoni:ital,wght@0,700;1,700&display=swap">
<style>
  :root {
    --backdrop: #1a1b1d;
    --card-light: #dedede;
    --card-mid: #a9a8a8;
    --card-dark: #5a5454;
    --band-light: #e8e8e8;
    --band-dark: #5e5858;
    --brand-gold: #a08f2c;
    --accent-gold: #f1d97c;
    --label-brown: #5a4334;
  }
  * { margin: 0; padding: 0; box-sizing: border-box; }
  html, body {
    width: 1200px;
    height: 1063px;
    overflow: hidden;
    background: var(--backdrop);
  }
  .card {
    position: absolute;
    left: 127px;
    top: 251px;
    width: 940px;
    height: 579px;
    border: 1px solid #cfcfcf;
    overflow: hidden;
    font-family: "Libre Bodoni", "Bodoni Moda", serif;
  }
  .card-face {
    position: absolute;
    inset: 0 0 140px 0;
    background: linear-gradient(to bottom,
      var(--card-light) 0%,
      var(--card-light) 30%,
      var(--card-mid) 55%,
      var(--card-dark) 100%);
  }
  .contact-band {
    position: absolute;
    left: 0; right: 0; bottom: 0;
    height: 140px;
    background: linear-gradient(to bottom,
      var(--band-light) 0%,
      #cfcfcf 30%,
      #8f8b8b 75%,
      var(--band-dark) 100%);
  }
  .brand-name {
    position: absolute;
    left: 510px;
    top: 84px;
    transform: translateX(-50%);
    font-size: 52px;
    font-weight: 700;
    color: var(--brand-gold);
    letter-spacing: 1px;
    white-space: nowrap;
  }
  .employee {
    position: absolute;
    right: 128px;
    top: 352px;
    text-align: right;
    font-style: italic;
    font-weight: 700;
    font-size: 25px;
    line-height: 34px;
    color: var(--accent-gold);
  }
  .contact-field {
    position: absolute;
    font-style: italic;
    font-weight: 700;
    font-size: 24px;
    color: var(--label-brown);
    white-space: nowrap;
  }
  .field-phone   { left: 79px;  top: 466px; }
  .field-fax     { left: 254px; top: 466px; }
  .field-address { left: 459px; top: 466px; }
  .field-email   { left: 79px;  top: 502px; }
  .field-website { left: 256px; top: 502px; }
</style>
</head>
<body>
  <div class="card">
    <div class="card-face"></div>
    <div class="contact-band"></div>

    <div class="brand-name">Aldermere Law</div>

    <div class="employee">
      <div class="employee-name">Employee Name</div>
      <div class="employee-title">Job Title</div>
    </div>

    <div class="contact-field field-phone">Phone:</div>
    <div class="contact-field field-fax">Facsimile:</div>
    <div class="contact-field field-address">Address:</div>
    <div class="contact-field field-email">e-mail:</div>
    <div class="contact-field field-website">website:</div>
  </div>
</body>
</html>
```